Looking for updated Letterhead and Compliments Slips to go with our new updated logo. This stationary will be used for letters to suppliers and customers so needs to be practical while also quite classic.

We are an engineering company so needs to be clean and precise

Target Market(s)

SME'S and large automotive customers

Industry/Entity Type

Automotive

Font styles to use
Sans Serif

Colors
85acd3
0356a4
0792cd
33a6d7
85abd2
ffffff

Requirements
Must have
• Address details as below
• KT Fabrications Limited
• Hallmere Road
• Ashbrook
• Fenshire
• LP47 9XZ, UK
• Telephone: +44 (0)1632 960418
• Fax: +44 (0)1632 960733
• Email: sales@ktfabrications.example
• Web: www.ktfabrications.example
Nice to have
• Nice to have some element of being a British Manufacturer

```html
<!DOCTYPE html>
<html lang="en">
<head>
<meta charset="utf-8">
<title>KT Fabrications Stationery</title>
<link href="https://fonts.googleapis.com/css2?family=Source+Sans+3:wght@400;500;600&display=swap" rel="stylesheet">
<style>
  :root {
    --navy: #0a3d8c;
    --band: #0356a4;
    --sky: #85acd3;
    --ink: #2a2a2a;
    --paper: #ffffff;
    --backdrop: #e9e9e9;
  }
  * { box-sizing: border-box; margin: 0; padding: 0; }
  html, body { width: 1200px; height: 831px; overflow: hidden; }
  body {
    background: var(--backdrop);
    font-family: "Source Sans 3", Arial, sans-serif;
    color: var(--ink);
    position: relative;
  }
  .sheet {
    position: absolute;
    background: var(--paper);
    box-shadow: 0 2px 10px rgba(0,0,0,0.12);
  }
  .letterhead { left: 50px; top: 35px; width: 538px; height: 761px; }
  .slip { left: 620px; top: 35px; width: 540px; height: 256px; }

  .brand { position: absolute; display: flex; align-items: center; gap: 8px; }
  .brand-name {
    font-weight: 600;
    color: var(--navy);
    letter-spacing: 0.32em;
    white-space: nowrap;
  }
  .brand-dot { border-radius: 50%; background: var(--sky); flex: none; }

  .letterhead .brand { left: 56px; top: 62px; }
  .letterhead .brand-name { font-size: 15px; }
  .letterhead .brand-dot { width: 12px; height: 12px; }

  .slip .brand { left: 26px; top: 76px; }
  .slip .brand-name { font-size: 13px; }
  .slip .brand-dot { width: 10px; height: 10px; }

  .slip-title {
    position: absolute; right: 22px; top: 52px;
    font-size: 19px; color: var(--band); font-weight: 400;
  }

  .address { position: absolute; font-size: 10.5px; line-height: 1.35; }
  .letterhead .address { right: 30px; bottom: 58px; text-align: right; }
  .slip .address { left: 0; right: 0; bottom: 46px; text-align: center; }

  .contact-band {
    position: absolute; left: 0; right: 0;
    background: var(--band);
    border-top: 2px solid var(--navy);
    display: flex; align-items: center; justify-content: center; gap: 10px;
    color: var(--paper); font-size: 10px; white-space: nowrap;
  }
  .contact-band::after {
    content: ""; position: absolute; left: 0; right: 0; bottom: -4px;
    height: 1px; background: var(--navy);
  }
  .letterhead .contact-band { bottom: 22px; height: 24px; gap: 8px; font-size: 9.2px; }
  .slip .contact-band { bottom: 20px; height: 22px; }

  .contact { display: flex; align-items: center; gap: 4px; }
  .contact svg { width: 10px; height: 10px; fill: none; stroke: var(--paper); stroke-width: 1.4; }
</style>
</head>
<body>

<section class="sheet letterhead" aria-label="Letterhead">
  <div class="brand"><span class="brand-dot"></span><span class="brand-name">KT FABRICATIONS</span></div>
  <div class="address">
    <p>KT Fabrications Limited</p>
    <p>Hallmere Road , Ashbrook, Fenshire LP47 9XZ, UK</p>
  </div>
  <div class="contact-band">
    <span class="contact"><svg viewBox="0 0 12 12"><path d="M3 1.5l2 2.2-1.2 1.4a6 6 0 0 0 3.1 3.1L8.3 7l2.2 2-1.4 1.5C5 10 2 7 1.5 2.9z"/></svg>+44 (0)1632 960418</span>
    <span class="contact"><svg viewBox="0 0 12 12"><rect x="2" y="4.5" width="8" height="5"/><path d="M3.5 4.5V1.5h5v3"/></svg>+44 (0)1632 960733</span>
    <span class="contact"><svg viewBox="0 0 12 12"><rect x="1" y="2.5" width="10" height="7"/><path d="M1 2.5l5 4 5-4"/></svg>sales@ktfabrications.example</span>
    <span class="contact"><svg viewBox="0 0 12 12"><circle cx="6" cy="6" r="4.8"/><path d="M1.2 6h9.6M6 1.2c-2.6 3-2.6 6.6 0 9.6M6 1.2c2.6 3 2.6 6.6 0 9.6"/></svg>www.ktfabrications.example</span>
  </div>
</section>

<section class="sheet slip" aria-label="Compliments slip">
  <div class="brand"><span class="brand-dot"></span><span class="brand-name">KT FABRICATIONS</span></div>
  <h1 class="slip-title">With Compliments</h1>
  <div class="address">
    <p>KT Fabrications Limited</p>
    <p>Hallmere Road , Ashbrook, Fenshire LP47 9XZ, UK</p>
  </div>
  <div class="contact-band">
    <span class="contact"><svg viewBox="0 0 12 12"><path d="M3 1.5l2 2.2-1.2 1.4a6 6 0 0 0 3.1 3.1L8.3 7l2.2 2-1.4 1.5C5 10 2 7 1.5 2.9z"/></svg>+44 (0)1632 960418</span>
    <span class="contact"><svg viewBox="0 0 12 12"><rect x="2" y="4.5" width="8" height="5"/><path d="M3.5 4.5V1.5h5v3"/></svg>+44 (0)1632 960733</span>
    <span class="contact"><svg viewBox="0 0 12 12"><rect x="1" y="2.5" width="10" height="7"/><path d="M1 2.5l5 4 5-4"/></svg>sales@ktfabrications.example</span>
    <span class="contact"><svg viewBox="0 0 12 12"><circle cx="6" cy="6" r="4.8"/><path d="M1.2 6h9.6M6 1.2c-2.6 3-2.6 6.6 0 9.6M6 1.2c2.6 3 2.6 6.6 0 9.6"/></svg>www.ktfabrications.example</span>
  </div>
</section>

</body>
</html>
```